Editorial Website Design for High-End Custom Millwork Firm

Design (no development) for a 5-7 page website for a high-end custom architectural millwork firm. Editorial, magazine-quality aesthetic — think Dwelling Quarterly and top-tier millwork studios (Owen Tallard, Vorko). Full brief, reference sites, and project photography attached. We have uploaded a sample of our photography to use in your design. PLEASE READ PDF DOCUMENT BRIEF!!!

```html
<!DOCTYPE html>
<html lang="en">
<head>
<meta charset="utf-8">
<title>Oakline — Custom Architectural Millwork</title>
<link href="https://fonts.googleapis.com/css2?family=Libre+Caslon+Display&family=Poppins:wght@300;400;500&display=swap" rel="stylesheet">
<style>
:root{
  --black:#000;
  --ink:#0a0a0a;
  --white:#fff;
  --paper:#f2f1ee;
  --card:#f5f5f4;
  --taupe:#4a453f;
  --pill:#5a5650;
  --pill-light:#d8d5d0;
  --tan:#b9ad97;
  --muted:#9a948c;
  --text-dark:#2a2723;
  --line:#8c857b;
  --serif:"Libre Caslon Display", "Times New Roman", serif;
  --sans:"Poppins", Arial, sans-serif;
}
*{box-sizing:border-box;margin:0;padding:0}
html,body{width:1200px;height:5391px;overflow:hidden;background:var(--black);font-family:var(--sans);color:var(--white)}
.page{position:relative;width:1200px;height:5391px}
section,footer{position:absolute;left:0;width:1200px;overflow:hidden}
.abs{position:absolute}
.center{left:0;width:100%;text-align:center}
.eyebrow{font-size:10px;letter-spacing:.3px;text-transform:uppercase;color:var(--muted)}
.title{font-family:var(--serif);font-weight:400;text-transform:uppercase;letter-spacing:.5px}
.tick{position:absolute;left:50%;width:1px;height:18px;background:var(--line)}
.rule{position:absolute;height:1px;background:var(--line)}
.pill{position:absolute;display:flex;align-items:center;justify-content:center;gap:8px;height:44px;border-radius:22px;font-size:11px;text-transform:uppercase;letter-spacing:.3px;color:var(--white);background:var(--pill)}
.pill.light{background:var(--pill-light);color:var(--text-dark)}
.pill svg{width:9px;height:9px}
.photo{position:absolute}
.circle-arrow{position:absolute;width:18px;height:18px;border-radius:50%;background:#8d8780;display:flex;align-items:center;justify-content:center}
.circle-arrow svg{width:8px;height:8px}

.hero{top:0;height:693px}
.hero .photo{inset:0;background:radial-gradient(ellipse at 50% 45%,#6a5a47 0%,#3a3129 45%,#1a1714 100%)}
.hero .shade{position:absolute;inset:0;background:linear-gradient(180deg,rgba(0,0,0,.35),rgba(0,0,0,.15) 40%,rgba(0,0,0,.4))}
.nav{position:absolute;top:22px;left:0;width:100%;height:40px}
.logo{position:absolute;left:124px;top:0;height:36px;width:82px;background:#8a8378;display:flex;align-items:center;justify-content:center;font-family:var(--serif);font-size:15px;color:var(--white);letter-spacing:1px}
.menu{position:absolute;left:535px;top:11px;display:flex;gap:22px;font-size:11px;text-transform:uppercase}
.menu .on{font-weight:500}
.call{position:absolute;left:960px;top:0;width:120px;height:42px;border-radius:21px;background:#6c6964;font-size:11px;display:flex;align-items:center;justify-content:center;gap:6px}
.nav .bar{position:absolute;top:60px;left:0;width:100%;height:1px;background:rgba(255,255,255,.25)}
.hero h1{position:absolute;top:244px;font-family:var(--serif);font-weight:400;font-size:46px;letter-spacing:.5px}
.hero .tagbox{position:absolute;top:308px;left:373px;width:480px;height:58px;background:rgba(170,160,140,.8);display:flex;align-items:center;justify-content:center;font-family:var(--serif);font-size:44px;letter-spacing:1px}
.hero p{position:absolute;top:384px;font-size:14px;line-height:22px}
.dots{position:absolute;display:flex;gap:6px}
.dots i{width:9px;height:9px;border-radius:50%;background:#aaa}
.dots i.on{background:#fff}

.services{top:693px;height:551px;background:var(--black)}
.card{position:absolute;top:201px;width:308px;height:235px;border-radius:14px;background:var(--card);box-shadow:0 0 0 4px rgba(255,255,255,.12);color:var(--text-dark);padding:48px 28px 0}
.card svg.ico{width:32px;height:32px}
.card h3{font-family:var(--serif);font-weight:400;font-size:19px;margin:14px 0 6px}
.card p{font-size:11px;line-height:20px;color:#555}
.card .circle-arrow{right:28px;bottom:34px}

.about{top:1244px;height:592px;background:var(--ink)}
.about .left{left:0;top:0;width:465px;height:482px;border-radius:0 0 22px 0;background:linear-gradient(135deg,#5b4230,#2e2a2c 55%,#2b3548)}
.about .right{left:733px;top:0;width:467px;height:592px;background:linear-gradient(160deg,#3a3a2e,#1d2118 60%,#0f0f0e);opacity:.8}
.about .veil{position:absolute;left:200px;top:100px;width:800px;height:390px;background:rgba(0,0,0,.55);filter:blur(30px)}
.about p.body{position:absolute;top:212px;left:230px;width:740px;text-align:center;font-size:19px;line-height:32px}

.team{top:1836px;height:557px;background:var(--taupe)}
.team h2{position:absolute;left:121px;top:112px;font-family:var(--serif);font-weight:400;font-size:31px;line-height:46px;text-transform:uppercase}
.team p{position:absolute;left:121px;top:292px;width:340px;font-size:11px;line-height:21px;color:#ddd8d0}
.team .photo{left:557px;top:32px;width:519px;height:490px;border-radius:22px 0 22px 0;background:linear-gradient(150deg,#9a968d,#6d6a64 40%,#b9b0a0)}

.projects{top:2393px;height:710px;background:var(--paper);color:var(--text-dark)}
.proj{position:absolute;top:187px;width:471px;height:373px;border-radius:0 22px 0 0;overflow:hidden}
.proj .photo{inset:0}
.proj .meta{position:absolute;left:28px;bottom:60px;font-size:10px;color:#eee;display:flex;gap:24px}
.proj h3{position:absolute;left:28px;bottom:28px;font-family:var(--serif);font-weight:400;font-size:19px;color:#fff}
.proj .circle-arrow{right:22px;bottom:34px;background:rgba(255,255,255,.35)}

.portfolio{top:3103px;height:630px;background:var(--black)}
.gal{position:absolute;top:212px;height:280px}
.gal.feat{border-radius:22px 22px 0 0}
.gal h3{position:absolute;left:18px;bottom:16px;font-family:var(--serif);font-weight:400;font-size:20px}
.gal .circle-arrow{right:26px;bottom:20px;background:rgba(255,255,255,.35)}

.news{top:3733px;height:679px;background:var(--paper);color:var(--text-dark)}
.post{position:absolute;top:162px;width:302px}
.post .photo{position:relative;height:278px;border-radius:0 22px 0 0}
.post .date{font-size:10px;color:#8a8277;margin-top:22px}
.post h3{font-family:var(--serif);font-weight:400;font-size:19px;line-height:26px;margin-top:6px}
.post .rule{left:0;top:383px;width:280px}
.post .circle-arrow{right:0;top:374px}

.cta{top:4412px;height:473px;background:linear-gradient(120deg,#2a2724,#3a3632 50%,#24211f)}
.cta .shade{position:absolute;inset:0;background:rgba(20,18,16,.55)}
.cta h2{position:absolute;top:145px;font-size:32px;line-height:46px}
.cta p{position:absolute;top:247px;font-size:12px;line-height:20px;color:#ddd}

.footer{top:4885px;height:506px;background:var(--black)}
.footer .ghost{position:absolute;left:270px;top:330px;font-family:var(--serif);font-size:230px;color:rgba(255,255,255,.05);letter-spacing:20px;white-space:nowrap}
.footer .flogo{position:absolute;left:124px;top:126px;width:90px;height:38px;background:#8a8378;display:flex;align-items:center;justify-content:center;font-family:var(--serif);font-size:15px;letter-spacing:1px}
.footer .about-text{position:absolute;left:124px;top:194px;width:210px;font-size:10px;line-height:20px;color:var(--muted)}
.social{position:absolute;left:124px;top:282px;display:flex;gap:30px}
.social i{width:16px;height:16px;border-radius:50%;border:1.5px solid #fff}
.fcol h4{font-family:var(--serif);font-weight:400;font-size:14px;line-height:20px}
.fcol ul{list-style:none;margin-top:26px;font-size:10px;line-height:21px;color:var(--muted)}
.contact{display:flex;gap:18px;font-size:10px;line-height:20px;color:var(--muted);margin-top:14px}
.contact svg{width:11px;height:11px;flex:none;margin-top:4px}
.footer .line{position:absolute;left:124px;top:434px;width:955px;height:1px;background:#333}
.footer .copy{position:absolute;top:460px;font-size:10px;color:#bbb}
</style>
</head>
<body>
<div class="page">

<svg width="0" height="0" style="position:absolute">
  <defs>
    <symbol id="arrow" viewBox="0 0 10 10"><path d="M2 8 L8 2 M3 2 H8 V7" stroke="currentColor" stroke-width="1.5" fill="none"/></symbol>
  </defs>
</svg>

<section class="hero">
  <div class="photo" role="img" aria-label="Photograph of a boutique interior with arched millwork shelving and a round display table"></div>
  <div class="shade"></div>
  <header class="nav">
    <div class="logo">OAKLINE</div>
    <nav class="menu"><span class="on">Home</span><span>Projects</span><span>Case Study</span><span>Services</span><span>About</span><span>Blog</span></nav>
    <div class="call"><svg width="10" height="10" viewBox="0 0 24 24"><path fill="#fff" d="M6.6 10.8a15 15 0 006.6 6.6l2.2-2.2c.3-.3.7-.4 1-.2 1.1.4 2.3.6 3.6.6.6 0 1 .4 1 1V20c0 .6-.4 1-1 1A17 17 0 013 4c0-.6.4-1 1-1h3.5c.6 0 1 .4 1 1 0 1.3.2 2.5.6 3.6.1.3 0 .7-.2 1z"/></svg>555.014.2290</div>
    <div class="bar"></div>
  </header>
  <h1 class="center">A High-End Custom Architectural</h1>
  <div class="tagbox">MILLWORK FIRM</div>
  <p class="center">Our work has been featured in many national magazines and<br>photographed for syndicated use.</p>
  <div class="pill light" style="left:536px;top:453px;width:156px;height:50px;background:#d9d6d1">View Projects <svg><use href="#arrow"/></svg></div>
  <div class="dots" style="left:584px;top:616px"><i></i><i></i><i class="on"></i><i></i></div>
</section>

<section class="services">
  <div class="abs center eyebrow" style="top:74px">Our Services</div>
  <h2 class="abs center title" style="top:100px;font-size:30px">Browse Our Set Of Services</h2>
  <div class="rule" style="left:413px;top:152px;width:374px"></div>
  <div class="tick" style="top:144px"></div>

  <div class="card" style="left:119px">
    <svg class="ico" viewBox="0 0 32 32" fill="none" stroke="#222" stroke-width="1.5"><rect x="6" y="8" width="20" height="18"/><path d="M6 14h20M6 20h20M16 8v18M4 26h24M10 4h12v4"/></svg>
    <h3>Interior Design</h3>
    <p>Lorem Ipsum Has Been The Industry's Standard Dummy Text Ever Since</p>
    <div class="circle-arrow" style="color:#fff"><svg><use href="#arrow"/></svg></div>
  </div>
  <div class="card" style="left:446px">
    <svg class="ico" viewBox="0 0 32 32" fill="none" stroke="#222" stroke-width="1.5"><rect x="9" y="4" width="14" height="22"/><path d="M12 9h3M17 9h3M12 14h3M17 14h3M12 19h3M17 19h3M5 28h22"/></svg>
    <h3>Exterior Design</h3>
    <p>Lorem Ipsum Has Been The Industry's Standard Dummy Text Ever Since</p>
    <div class="circle-arrow" style="color:#fff"><svg><use href="#arrow"/></svg></div>
  </div>
  <div class="card" style="left:773px">
    <svg class="ico" viewBox="0 0 32 32" fill="none" stroke="#222" stroke-width="1.5"><path d="M6 28V14a10 10 0 0120 0v14M11 28V15a5 5 0 0110 0v13M4 28h24"/></svg>
    <h3>Architectural Design</h3>
    <p>Lorem Ipsum Has Been The Industry's Standard Dummy Text Ever Since</p>
    <div class="circle-arrow" style="color:#fff"><svg><use href="#arrow"/></svg></div>
  </div>

  <div class="pill" style="left:492px;top:455px;width:188px;height:50px">Creat Custom Design <svg><use href="#arrow"/></svg></div>
</section>

<section class="about">
  <div class="photo left" role="img" aria-label="Photograph of a warm lounge with carved wooden screen panels and velvet seating"></div>
  <div class="photo right" role="img" aria-label="Photograph of a dim interior with a green living wall and wood paneling"></div>
  <div class="veil"></div>
  <div class="abs center eyebrow" style="top:104px">About Oakline Residential</div>
  <h2 class="abs center title" style="top:128px;font-size:30px">A Privately Held Company</h2>
  <div class="tick" style="top:168px"></div>
  <p class="body">We Are A Privately Held Company With A Long-Standing Tradition Of Employee Ownership. We Draw On This Area's History Of Fine Furniture Making And Have Attracted Skilled Craftsmen And Finish People From All Over The Country From London, New York City, And Beyond.</p>
  <div class="pill" style="left:522px;top:370px;width:156px;height:40px;background:#555049">More About Us <svg><use href="#arrow"/></svg></div>
</section>

<section class="team">
  <div class="abs eyebrow" style="left:121px;top:92px;color:#bdb5aa">Our Team</div>
  <h2>The Talent And<br>Expertise To Handle<br>Every Aspect</h2>
  <p>With An Average Of Eleven Years Employment, Our Truly Dedicated Staff Is Our Strongest Asset. Our Family-Like Atmosphere Has Helped Us Grow Not Only In Size But In Quality And Complexity Of Cabinetry As Well.</p>
  <div class="pill" style="left:121px;top:400px;width:156px;height:38px;background:#6d675f">Our Team <svg><use href="#arrow"/></svg></div>
  <div class="photo" role="img" aria-label="Photograph of a craftsman assembling a lattice cabinet panel in the workshop"></div>
</section>

<section class="projects">
  <div class="abs center eyebrow" style="top:52px;color:#a89c88">Case Study</div>
  <h2 class="abs center title" style="top:76px;font-size:30px">Last Projects We Designed</h2>
  <div class="rule" style="left:413px;top:126px;width:374px"></div>
  <div class="tick" style="top:120px"></div>

  <article class="proj" style="left:119px">
    <div class="photo" role="img" aria-label="Photograph of grey kitchen cabinetry with glass-front upper doors" style="background:linear-gradient(180deg,#d7d4cd,#8e8b84 60%,#3b3936)"></div>
    <div class="meta"><span>03 July, 2026</span><span>New York City</span></div>
    <h3>The Modern Grey Kitchen</h3>
    <div class="circle-arrow" style="color:#fff"><svg><use href="#arrow"/></svg></div>
  </article>
  <article class="proj" style="left:609px">
    <div class="photo" role="img" aria-label="Photograph of a white kitchen with walnut cabinets and glass display uppers" style="background:linear-gradient(180deg,#8a5a36,#c49a72 45%,#5a3a22)"></div>
    <div class="meta"><span>03 July, 2026</span><span>New York City</span></div>
    <h3>TheModern White Kitchen</h3>
    <div class="circle-arrow" style="color:#fff"><svg><use href="#arrow"/></svg></div>
  </article>

  <div class="pill light" style="left:541px;top:611px;width:156px;height:42px">View All <svg><use href="#arrow"/></svg></div>
</section>

<section class="portfolio">
  <div class="abs center eyebrow" style="top:76px;color:#a89c88">Portfolio</div>
  <h2 class="abs center title" style="top:100px;font-size:30px;left:-12px">Explore Oakline Cabinetry</h2>
  <div class="photo gal" role="img" aria-label="Photograph of an arched built-in hutch with blue and white china" style="left:0;width:155px;background:linear-gradient(180deg,#e4e1db,#9d9a92)"></div>
  <div class="photo gal" role="img" aria-label="Photograph of walnut kitchen cabinets with lit glass uppers" style="left:168px;width:201px;background:linear-gradient(180deg,#a26a3e,#d8b48e 50%,#6b4226)"></div>
  <div class="photo gal feat" role="img" aria-label="Photograph of a dark wood interior with a mosaic feature wall and green plants" style="left:381px;width:436px;background:linear-gradient(90deg,#4a2e1c,#8d7766 45%,#2f4a2a 75%,#3a2618)">
    <h3>The Modern Grey Kitchen</h3>
    <div class="circle-arrow" style="color:#fff"><svg><use href="#arrow"/></svg></div>
  </div>
  <div class="photo gal" role="img" aria-label="Photograph of a white kitchen with a pendant lantern and blue chairs" style="left:831px;width:201px;background:linear-gradient(180deg,#e7e6e2,#7b8a99)"></div>
  <div class="photo gal" role="img" aria-label="Photograph of a bright open kitchen with island and wood beams" style="left:1045px;width:155px;background:linear-gradient(180deg,#cdb89a,#efece6)"></div>
  <div class="dots" style="left:568px;top:548px"><i></i><i></i><i class="on"></i><i></i></div>
</section>

<section class="news">
  <div class="abs center eyebrow" style="top:38px;color:#a89c88;left:-12px">Case Study</div>
  <h2 class="abs center title" style="top:66px;font-size:30px;left:-12px">Browse Our Articles &amp; News</h2>
  <div class="rule" style="left:401px;top:118px;width:374px"></div>
  <div class="tick" style="top:112px;left:588px"></div>

  <article class="post" style="left:119px">
    <div class="photo" role="img" aria-label="Photograph of a showroom with coffered ceiling and wood display cabinets" style="background:linear-gradient(180deg,#3a332c,#8a7358 55%,#4a3a2a)"></div>
    <div class="date">JULY 03</div>
    <h3>Spring News From Oakline<br>Design Studio</h3>
    <div class="rule"></div>
    <div class="circle-arrow" style="color:#fff"><svg><use href="#arrow"/></svg></div>
  </article>
  <article class="post" style="left:448px">
    <div class="photo" role="img" aria-label="Photograph of an arched hutch with china and flowers" style="background:linear-gradient(180deg,#e2ded6,#9a9890 60%,#5e6b7a)"></div>
    <div class="date">JULY 03</div>
    <h3>Spring News From Oakline<br>Design Studio</h3>
    <div class="rule"></div>
    <div class="circle-arrow" style="color:#fff"><svg><use href="#arrow"/></svg></div>
  </article>
  <article class="post" style="left:777px">
    <div class="photo" role="img" aria-label="Photograph of a kitchen with warm wood cabinetry and pendant lights" style="background:linear-gradient(180deg,#e8ddd0,#b47a4a 55%,#6a4428)"></div>
    <div class="date">JULY 03</div>
    <h3>Spring News From Oakline<br>Design Studio</h3>
    <div class="rule"></div>
    <div class="circle-arrow" style="color:#fff"><svg><use href="#arrow"/></svg></div>
  </article>

  <div class="pill light" style="left:513px;top:574px;width:156px;height:42px">View All <svg><use href="#arrow"/></svg></div>
</section>

<section class="cta">
  <div class="photo" role="img" aria-label="Photograph of a workshop bench with lattice panels in progress" style="inset:0"></div>
  <div class="shade"></div>
  <h2 class="center title">Ready To Take It A Step<br>Further</h2>
  <p class="center">Let's Start Purchasing Framewright Theme And Find Out How It Can Help Create Your<br>Business Website</p>
  <div class="pill" style="left:522px;top:316px;width:156px;height:42px;background:#6d6862">Contact Us <svg><use href="#arrow"/></svg></div>
</section>

<footer class="footer">
  <div class="ghost">OAKLINE</div>
  <div class="flogo">OAKLINE</div>
  <p class="about-text">Your Leader In Kitchen Design &amp; Remodeling · Specializing In Quality Cabinets That's Built To Last.</p>
  <div class="social"><i></i><i></i><i></i><i></i></div>

  <div class="abs fcol" style="left:394px;top:124px">
    <h4>Quick Link</h4>
    <ul><li>Home</li><li>Projects</li><li>Case Study</li><li>Services</li><li>About</li><li>Blog</li></ul>
  </div>
  <div class="abs fcol" style="left:555px;top:124px;width:250px">
    <h4>Fairhaven Showroom And Custom Cabinetry Shop:</h4>
    <div class="contact"><svg viewBox="0 0 24 24" fill="#9a948c"><path d="M12 2a7 7 0 00-7 7c0 5 7 13 7 13s7-8 7-13a7 7 0 00-7-7zm0 9.5A2.5 2.5 0 1112 6.5a2.5 2.5 0 010 5z"/></svg><span>48 Alder Row<br>Fairhaven, ST 20410</span></div>
    <div class="contact"><svg viewBox="0 0 24 24" fill="#9a948c"><path d="M6.6 10.8a15 15 0 006.6 6.6l2.2-2.2c.3-.3.7-.4 1-.2 1.1.4 2.3.6 3.6.6.6 0 1 .4 1 1V20c0 .6-.4 1-1 1A17 17 0 013 4c0-.6.4-1 1-1h3.5c.6 0 1 .4 1 1 0 1.3.2 2.5.6 3.6.1.3 0 .7-.2 1z"/></svg><span>555-014-3377</span></div>
    <div class="contact"><svg viewBox="0 0 24 24" fill="none" stroke="#9a948c" stroke-width="2"><rect x="3" y="5" width="18" height="14"/><path d="M3 5l9 8 9-8"/></svg><span>Hello@Oaklinestudio.com</span></div>
  </div>
  <div class="abs fcol" style="left:844px;top:124px;width:250px">
    <h4>Brightwater Custom Cabinetry<br>Showroom:</h4>
    <div class="contact"><svg viewBox="0 0 24 24" fill="#9a948c"><path d="M12 2a7 7 0 00-7 7c0 5 7 13 7 13s7-8 7-13a7 7 0 00-7-7zm0 9.5A2.5 2.5 0 1112 6.5a2.5 2.5 0 010 5z"/></svg><span>702 Harbor Lane<br>Brightwater, ST 20588</span></div>
    <div class="contact"><svg viewBox="0 0 24 24" fill="#9a948c"><path d="M6.6 10.8a15 15 0 006.6 6.6l2.2-2.2c.3-.3.7-.4 1-.2 1.1.4 2.3.6 3.6.6.6 0 1 .4 1 1V20c0 .6-.4 1-1 1A17 17 0 013 4c0-.6.4-1 1-1h3.5c.6 0 1 .4 1 1 0 1.3.2 2.5.6 3.6.1.3 0 .7-.2 1z"/></svg><span>555-018-4410</span></div>
    <div class="contact"><svg viewBox="0 0 24 24" fill="none" stroke="#9a948c" stroke-width="2"><rect x="3" y="5" width="18" height="14"/><path d="M3 5l9 8 9-8"/></svg><span>Studio@Oaklinestudio.com</span></div>
  </div>

  <div class="line"></div>
  <div class="copy center">©2026 <span style="color:#b9ad97">Oaklinestudio.com</span>,All Right Reserved</div>
</footer>

</div>
</body>
</html>
```